Business Cards for Internet Security Company

Awesome designers! This is the opportunity to help design cards for a forward thinking network security company. They use threat information gathered from peer groups to make intelligent decisions on what threats are relevant and which arent. ( not that you need this to do designs, but just so you know where they are coming from. ) :-)

We'd like to see a two side design and the deliverables will be in illustrator 4. The logo is attached and the logo colors are attached in the JPG and I've attached a an eps of the logo and icon

Security

```html
<!DOCTYPE html>
<html lang="en">
<head>
<meta charset="UTF-8">
<title>Torvane Business Cards</title>
<link href="https://fonts.googleapis.com/css2?family=Source+Sans+3:wght@400;600&display=swap" rel="stylesheet">
<style>
  :root {
    --backdrop: #e6e8eb;
    --card: #ffffff;
    --ink: #1f5878;
    --ink-soft: #3a6d8c;
    --brand: #2f6f99;
    --accent: #4a8cc8;
    --ghost: #dfe6ef;
    --rule: #d7dde3;
  }
  * { margin: 0; padding: 0; box-sizing: border-box; }
  html, body {
    width: 1200px; height: 900px; overflow: hidden;
    background: var(--backdrop);
    font-family: "Source Sans 3", "Myriad Pro", sans-serif;
    color: var(--ink);
  }
  .stage { position: relative; width: 1200px; height: 900px; }
  .card {
    position: absolute;
    width: 560px; height: 320px;
    background: var(--card);
    box-shadow: 0 6px 20px rgba(0,0,0,.12);
    overflow: hidden;
  }
  .card-front { left: 70px; top: 90px; }
  .card-back { left: 570px; top: 490px; }
  .ghost-ring {
    position: absolute;
    border-radius: 50%;
    border: 34px solid var(--ghost);
  }
  .card-front .ghost-ring { width: 300px; height: 300px; left: 150px; top: 10px; }
  .card-back .ghost-ring { width: 280px; height: 280px; left: 190px; top: 30px; }
  .brand {
    position: absolute;
    display: flex; align-items: center;
    color: var(--brand);
    font-weight: 600;
    letter-spacing: .5px;
  }
  .brand-dot {
    border-radius: 50%;
    background: var(--accent);
    flex: none;
  }
  .card-front .brand { left: 70px; top: 112px; font-size: 76px; gap: 16px; }
  .card-front .brand-dot { width: 56px; height: 56px; }
  .card-back .brand { left: 28px; top: 22px; font-size: 38px; gap: 9px; }
  .card-back .brand-dot { width: 28px; height: 28px; }
  .person { position: absolute; left: 30px; top: 96px; }
  .person-name { font-size: 26px; font-weight: 400; color: var(--ink); line-height: 1.1; }
  .person-title { font-size: 17px; font-style: italic; color: var(--ink-soft); }
  .address {
    position: absolute; left: 30px; top: 168px;
    font-size: 14px; line-height: 1.3; color: var(--ink-soft);
    list-style: none;
  }
  .contact {
    position: absolute; left: 270px; top: 230px;
    list-style: none; font-size: 16px; color: var(--ink);
  }
  .contact li, .address li { display: flex; align-items: center; gap: 7px; }
  .icon { width: 15px; height: 15px; fill: none; stroke: var(--ink); stroke-width: 1.6; flex: none; }
  .rule {
    position: absolute; left: 30px; right: 30px; bottom: 22px;
    height: 1px; background: var(--rule);
  }
</style>
</head>
<body>
<main class="stage">
  <section class="card card-front" aria-label="Card front">
    <div class="ghost-ring"></div>
    <div class="brand"><span class="brand-dot"></span>Torvane</div>
  </section>

  <section class="card card-back" aria-label="Card back">
    <div class="ghost-ring"></div>
    <div class="brand"><span class="brand-dot"></span>Torvane</div>
    <div class="person">
      <p class="person-name">Daniel Rourke</p>
      <p class="person-title">Managing Director</p>
    </div>
    <ul class="address">
      <li>418 Meridian Park Dr</li>
      <li>Fairview, MO 63021</li>
      <li>
        <svg class="icon" viewBox="0 0 16 16"><rect x="4" y="1.5" width="8" height="13" rx="1.5"/><line x1="7" y1="12" x2="9" y2="12"/></svg>
        555-201-4410
      </li>
    </ul>
    <ul class="contact">
      <li>
        <svg class="icon" viewBox="0 0 16 16"><rect x="4" y="1.5" width="8" height="4"/><rect x="1.5" y="5.5" width="13" height="6" rx="1"/><rect x="4" y="9.5" width="8" height="5"/></svg>
        555-201-4488
      </li>
      <li>
        <svg class="icon" viewBox="0 0 16 16"><rect x="1.5" y="3.5" width="13" height="9"/><polyline points="1.5,3.5 8,9 14.5,3.5"/></svg>
        d.rourke@torvanesecure.com
      </li>
    </ul>
    <div class="rule"></div>
  </section>
</main>
</body>
</html>
```